Company Playbill Advertisement Design

I own a production company that provides audio,lighting,video, and other production services to events and conventions. I am sponsoring a event and they are giving me a full page ad in the playbill. It needs to be Full Page (Full Bleed) Trim Area: 5.5” x 8.5” Image Area: 5” x 8”. I would like the design to include photos, information about my company, and my logo in a professional presentation to lure potential clients to contact us. We are a production company so it needs to be something that catches your eye but professional.

Target Market(s)

Companies looking for production services. Our customer is mainly a professional person looking for services. We are not a DJ company so our market is a bit smaller.

Industry/Entity Type

Events

Requirements
Must have
• Company phone number is 555-704-2981, website is www.brivanstagecrew.example. Company Logo, photos of events.
• Accepted Ad Formats: .jpg, .pdf., .eps. Full Color Minimum 300 dpi All Fonts Outlined. It needs to be Full Page (Full Bleed) Trim Area: 5.5” x 8.5” Image Area: 5” x 8”.
Nice to have
• Creative design that catches someone eye. We are a creative company so we want our ad to reflect that.

```html
<!DOCTYPE html>
<html lang="en">
<head>
<meta charset="utf-8">
<title>Brivan Stage Crew – Playbill Ad</title>
<link href="https://fonts.googleapis.com/css2?family=Archivo+Black&family=Open+Sans:wght@400;600;700;800&display=swap" rel="stylesheet">
<style>
  :root {
    --ink: #0e0e0e;
    --paper: #ffffff;
    --accent-red: #e01b24;
    --stage-dark: #0b1a18;
    --stage-teal: #2fa58f;
    --stage-glow: #9fe6d6;
    --band: #111111;
    --body-text: #2a2a2a;
  }
  * { margin: 0; padding: 0; box-sizing: border-box; }
  html, body { width: 777px; height: 1200px; overflow: hidden; background: var(--paper); }
  body { font-family: "Open Sans", Arial, sans-serif; color: var(--ink); }
  .ad { position: relative; width: 777px; height: 1200px; overflow: hidden; background: var(--paper); }

  .hero-photo {
    position: absolute; left: 0; top: 0; width: 777px; height: 581px;
    background:
      radial-gradient(ellipse 45% 35% at 50% 48%, var(--stage-glow) 0%, rgba(47,165,143,0.6) 40%, transparent 75%),
      radial-gradient(ellipse 70% 50% at 50% 35%, rgba(47,165,143,0.55), transparent 80%),
      linear-gradient(180deg, #0f2a26 0%, var(--stage-teal) 45%, #1a3f38 78%, var(--stage-dark) 100%);
  }
  .headline {
    position: absolute; left: 54px; top: 58px;
    font-family: "Archivo Black", "Arial Black", sans-serif;
    font-size: 29px; line-height: 35px; color: var(--paper); letter-spacing: 0.3px;
  }
  .headline span { display: inline-block; background: rgba(15,15,15,0.82); padding: 0 8px; }
  .headline .punch { color: var(--accent-red); background: none; }
  .brand-top {
    position: absolute; right: 56px; top: 62px;
    font-family: "Open Sans", sans-serif; font-weight: 800;
    font-size: 17px; color: var(--paper); display: flex; align-items: center; gap: 7px;
  }
  .brand-mark { width: 12px; height: 12px; background: currentColor; }

  .who-band {
    position: absolute; left: 0; top: 581px; width: 777px; height: 79px;
    background: var(--band); color: var(--paper);
  }
  .who-label {
    position: absolute; left: 52px; top: 66px; transform: rotate(-90deg); transform-origin: left top;
    font-family: "Archivo Black", sans-serif; line-height: 1;
  }
  .who-label b { font-size: 17px; display: block; }
  .who-label small { font-size: 8px; display: block; }
  .who-text {
    position: absolute; left: 113px; top: 12px; width: 620px;
    font-size: 14.2px; line-height: 18px;
  }

  .what-title {
    position: absolute; left: 54px; top: 678px;
    font-family: "Archivo Black", sans-serif; font-size: 41px; line-height: 50px;
    display: flex; align-items: center; gap: 6px;
  }
  .what-title .stack { font-size: 14px; line-height: 13px; text-align: center; }

  .service-list { position: absolute; top: 748px; width: 290px; }
  .service-list.left { left: 54px; }
  .service-list.right { right: 54px; top: 752px; text-align: right; width: 300px; }
  .service { margin-bottom: 10px; }
  .service-list.right .service { margin-bottom: 11px; }
  .service h3 { font-size: 21px; font-weight: 700; line-height: 24px; letter-spacing: 0.2px; }
  .service p { font-size: 12.5px; line-height: 14.5px; color: var(--body-text); }

  .brand-bottom {
    position: absolute; left: 54px; top: 1118px;
    font-family: "Open Sans", sans-serif; font-weight: 800;
    font-size: 20px; color: var(--ink); display: flex; align-items: center; gap: 8px;
  }
  .contact {
    position: absolute; right: 54px; top: 1110px; text-align: right;
    font-weight: 700; font-size: 21px; line-height: 25px;
  }
</style>
</head>
<body>
<div class="ad">
  <div class="hero-photo" role="img" aria-label="Festival stage photo with teal lighting beams, truss towers, an aerialist and a cheering crowd"></div>

  <h1 class="headline">
    <span>THE BEST SALES,</span><br>
    <span>PRODUCTION, AND</span><br>
    <span>RENTAL COMPANY</span><br>
    <span>YOU NEED IN</span><br>
    <span>CENTRAL FLORIDA.</span><br>
    <span class="punch">PERIOD.</span>
  </h1>

  <div class="brand-top"><span class="brand-mark"></span>Brivan Stage Crew</div>

  <section class="who-band">
    <div class="who-label"><b>WHO</b><small>WE ARE?</small></div>
    <p class="who-text">Brivan Stage Crew or BSC is your source for events, sales, production services, and entertainment in the Central Florida area. We can meet your needs in a hurry. We excel in the live event category with over 14 years experience in shows and festivals.</p>
  </section>

  <h2 class="what-title">WHAT <span class="stack">WE<br>DO</span>?</h2>

  <div class="service-list left">
    <div class="service"><h3>AUDIO SERVICES</h3><p>BSC has some of the best<br>audio gear so you can be heard</p></div>
    <div class="service"><h3>LIGHTING SERVICES</h3><p>We have the latest in automated<br>lighting fixtures</p></div>
    <div class="service"><h3>EVENT VIDEO</h3><p>BSC has a full line of LED walls<br>and projectors to fit any event and budget</p></div>
    <div class="service"><h3>EFFECTS</h3><p>Fog, Haze, Snow, Cryo C02, Confetti,<br>Pyro, Low Lying Fog</p></div>
    <div class="service"><h3>RIGGING</h3><p>We can elevate your event by providing<br>trussing, motors, or towers to hang<br>anything that needs to be put up</p></div>
  </div>

  <div class="service-list right">
    <div class="service"><h3>MOBILE / DECK STAGING</h3><p>We can provide any size mobile or<br>deck stage for your needs</p></div>
    <div class="service"><h3>EVENT MANAGEMENT</h3><p>We can take your event ideas<br>and make them a success</p></div>
    <div class="service"><h3>SALES AND INSTALL</h3><p>We provide the best gear for any situation<br>and will train you on how to use it</p></div>
    <div class="service"><h3>EQUIPMENT RENTALS</h3><p>BSC is a great source for rental gear.<br>Audio, Lighting, Video, LED Wall, Staging</p></div>
    <div class="service"><h3>EQUIPMENT RENTALS</h3><p>We partner with the award-winning team<br>at Lumenra Visual Productions on all video<br>and film production services</p></div>
  </div>

  <div class="brand-bottom"><span class="brand-mark"></span>Brivan Stage Crew</div>

  <div class="contact">
    <div>555-704-2981</div>
    <div>www.brivanstagecrew.example</div>
  </div>
</div>
</body>
</html>
```